Sehr bemüht, wollte unbedingt, dass ich uneingeschränkt zufrieden bin. Folgeaufträge werden jedenfalls folgen :-)
Zielgruppe
Ich bin Finanzberater und vermittle seit 28 Jahren Versicherungen, Geldanlagen und Finanzierungen. Meine Zielgruppe würde ich als „gehoben“ ansehen, viele haben leitende Positionen, sind Freiberufler, Akademiker ...
Für mich ist der ganzheitliche Beratungsansatz (alles aus einer Hand / ein Ansprechpartner für alle finanziellen Angelegenheiten) sehr wichtig, daher betreue ich viele Kunden schon 20 Jahre und länger.
Derzeit bin ich 57 Jahre alt, viele meiner Kunden in einem ähnlichen Alter. Viele meiner Kunden sind mit Versicherungen sehr gut ausgestattet, einige haben auch Wohnungseigentum (häufig mit mir finanziert).
Im jetzigen Alter ist jedenfalls Geldanlage / Vermögensplanung stark im Vordergrund und genau darauf möchte ich mein neues Visitenkartendesign ausrichten. Im Detail geht es mir um SACHWERT-Veranlagungen, weil aus meiner Sicht unfassbar viel Geld auf unverzinsten Sparkonten von der Inflation aufgefressen werden. Ziel meiner Kunden sollte es sein, mit Sachwertveranlagungen Erträge über der Inflation zu erzielen.
Ich habe laienhafte Graphiken hochgeladen, damit Sie einen ersten Eindruck bekommen.
Die Visitenkarte zeigt aus meiner sich von links nach rechts das gesamte „Kundenleben“.
Ganz links (egal ob das die Geburt oder der Einstieg ins Berufsleben ist) sind Versicherungen sehr wichtig, Der Vermögensaufbau startet ...
Wenn man auf der „Zeitachse“ Richtung Mitte geht, gehen Versicherungsthemen tendenziell zurück, Geldanlagen bleiben gleich breit / wichtig und das Finanzieren einer Immobilie könnte dazukommen.
Mit zunehmendem Alter (auf der Zeitachse weiter nach rechts) rücken Versicherungsthemen immer weiter in den Hintergrund ...
Botschaft meinerseits: Geldanlage (und hier v.a. Sachwertanlagen) sind das ganze Leben lang „gleich wichtig“ und damit kann ich Studenten genauso wie Berufstätige oder Pensionisten sehr gut ansprechen.
In Versicherungsangelegenheiten arbeite ich mit der LUPRIX GmbH ..
Aufgabenstellung
Folgende Inhalte müssen jedenfalls irgendwo auf der Visitenkarte (vorne oder hinten) zu finden sein:
Bereits bestehendes Logo
Mag. iur. Stefan Kolbeck
GF der Kolbeck & Partner GmbH
Finanzberater
Lindweg 117, 8071 Graz
Amt für HBR Graz, FN 517382k
stefan.kolbeck@kolbeckundpartner-muster.at
www.kolbeckundpartner-muster.at
BEVO 41726315 und 26850471
Abfrage BEVO: www.bevo-muster.at/vermittlerverzeichnis
Korrekter wäre es so, aber das ist halt sehr viel Text:
BEVO:
26850471 (Gewerbliche Vermögensberatung ohne Berechtigung zur Vermittlung von Lebens- und Unfallversicherungen & Berechtigung zur Tätigkeit als ungebundener Kreditvermittler)
41726315 (Versicherungsvermittlung in der Form Mehrfach-Versicherungsagent in Kooperation mit der LUPRIX GmbH
Die Visitenkarte soll eine 'typische' Größe haben, ich glaube das ist 8,5 x 5,5 cm?
Das Design sollte aufgrund der Klientel schon 'sehr gehoben' sein.
Ergänzend möchte ich erwähnen, dass ich meine Homepage und den Netzora-Banner / Header auf das neue Design anpassen möchte, vielleicht kann letzterer nach Fertigstellung der Visitenkarte bitte mit angeboten werden!?

```html
<!DOCTYPE html>
<html lang="de">
<head>
<meta charset="utf-8">
<title>Kolbeck und Partner – Visitenkarte</title>
<link rel="stylesheet" href="https://fonts.googleapis.com/css2?family=Arimo:wght@400;700&display=swap">
<style>
  :root {
    --card-bg: #231f1c;
    --gold: #e5b968;
    --white: #ffffff;
    --brand-red: #8a1c2b;
  }
  * { margin: 0; padding: 0; box-sizing: border-box; }
  html, body { width: 1200px; height: 686px; overflow: hidden; background: var(--card-bg); }
  .card {
    position: relative;
    width: 1200px; height: 686px;
    background: var(--card-bg);
    font-family: "Arimo", Arial, sans-serif;
    color: var(--white);
  }
  .brand-mark {
    position: absolute; left: 103px; top: 67px;
    width: 220px; height: 220px;
    background: var(--brand-red);
    border-radius: 8px;
  }
  .brand-name {
    position: absolute; left: 46px; top: 322px; width: 320px;
    text-align: center;
    color: var(--gold); font-weight: 700;
    font-size: 58px; line-height: 61px;
  }
  .brand-texture {
    position: absolute; left: 66px; top: 523px;
    width: 277px; height: 106px;
    background: radial-gradient(ellipse at 45% 50%, rgba(185,143,74,0.45), rgba(185,143,74,0) 70%);
  }
  .service {
    position: absolute; left: 478px; top: 52px; width: 600px;
    text-align: center; font-size: 64px; font-weight: 400; line-height: 1.15;
  }
  .divider {
    position: absolute; left: 585px; top: 160px;
    width: 403px; border-top: 2px dotted var(--gold);
  }
  .advisor {
    position: absolute; left: 434px; top: 162px; width: 700px;
    text-align: center; color: var(--gold);
    font-size: 56px; font-weight: 700; line-height: 1.15;
  }
  .contact { list-style: none; }
  .contact-icon { position: absolute; left: 420px; width: 34px; height: 34px; }
  .contact-text {
    position: absolute; left: 487px;
    font-size: 39px; line-height: 43px; white-space: nowrap;
  }
  .phone .contact-icon { top: 310px; }
  .phone .contact-text { top: 304px; }
  .email .contact-icon { top: 385px; }
  .email .contact-text { top: 381px; font-size: 33px; }
  .address .contact-icon { top: 454px; }
  .address .contact-text { top: 448px; }
  .web .contact-icon { top: 557px; }
  .web .contact-text { top: 553px; left: 493px; }
</style>
</head>
<body>
<div class="card">
  <div class="brand-mark" aria-hidden="true"></div>
  <div class="brand-name">Kolbeck<br>und<br>Partner</div>
  <div class="brand-texture" role="img" aria-label="Dekoratives goldenes Punktraster"></div>

  <h1 class="service">Finanzberatung</h1>
  <div class="divider"></div>
  <h2 class="advisor">Mag. iur. Stefan Kolbeck</h2>

  <ul class="contact">
    <li class="phone">
      <svg class="contact-icon" viewBox="0 0 34 34" aria-hidden="true"><circle cx="17" cy="17" r="17" fill="#e5b968"/><rect x="11.5" y="8" width="11" height="18" rx="2" fill="#231f1c"/><rect x="13.5" y="10.5" width="7" height="11" fill="#e5b968"/><circle cx="17" cy="23.5" r="1" fill="#e5b968"/></svg>
      <span class="contact-text">+43660 5128 394</span>
    </li>
    <li class="email">
      <svg class="contact-icon" viewBox="0 0 34 34" aria-hidden="true"><circle cx="17" cy="17" r="17" fill="#e5b968"/><rect x="9" y="11.5" width="16" height="11" rx="1.5" fill="#231f1c"/><path d="M9.5 12.5 L17 18 L24.5 12.5" fill="none" stroke="#e5b968" stroke-width="1.4"/></svg>
      <span class="contact-text">stefan.kolbeck@kolbeckundpartner-muster.at</span>
    </li>
    <li class="address">
      <svg class="contact-icon" viewBox="0 0 34 34" aria-hidden="true"><circle cx="17" cy="17" r="17" fill="#e5b968"/><path d="M17 8 C12.5 8 10.5 11.2 10.5 14 C10.5 18 17 26 17 26 C17 26 23.5 18 23.5 14 C23.5 11.2 21.5 8 17 8 Z" fill="#231f1c"/><circle cx="17" cy="14.3" r="2.6" fill="#e5b968"/></svg>
      <span class="contact-text">Lindweg 117/1<br>8071 Graz</span>
    </li>
    <li class="web">
      <svg class="contact-icon" viewBox="0 0 34 34" aria-hidden="true"><circle cx="17" cy="17" r="17" fill="#e5b968"/><g fill="none" stroke="#231f1c" stroke-width="1.6"><circle cx="17" cy="17" r="8"/><ellipse cx="17" cy="17" rx="3.5" ry="8"/><line x1="9" y1="17" x2="25" y2="17"/><line x1="10.5" y1="13" x2="23.5" y2="13"/><line x1="10.5" y1="21" x2="23.5" y2="21"/></g></svg>
      <span class="contact-text">www.kolbeckundpartner-muster.at</span>
    </li>
  </ul>
</div>
</body>
</html>
```